依頼概要
■ 依頼の目的/概要

弊社は「カード選びナビ広場 http://www.hoshizora-cardnavi.com/ 」というクレジットカードの比較サイトを運営しています。
今回はこのカード選びナビ広場のトップページのサイトデザインリニューアルをお願いします。

現在、サイト内( http://www.hoshizora-cardnavi.com/ )にある素材は自由に使って頂いて構いません。
既存のデザインを残しつつデザインをしていただいても
逆に完全新規にデザインをしていただいても構いません。
最終的なクオリティが高ければOKです。
素材サイトで何か素材を購入すればよりクオリティが高くなるのであれば
別途素材の購入も検討します。
その際はメッセージでご連絡ください。

■コーディング不要
コーディングは不要なので、デザインのみでOKです。

■ 希望するウェブデザイン

サイト訪問者が楽しくクレジットカードを選んだり
クレジットカードについての知識を学んだりできるようなデザインが希望です。
逆にサイト訪問者が堅苦しく感じてしまうようなデザインは避けたいです。
既存サイトでは下記URLのようなサイトデザインが好みです。

http://www.mz.tobira-net.com/mobile/index.html?bid=mz_gn_0007
http://www.mirumart.co.jp/kuruma/index.html?ca=top_glo_009
http://store.fenlow.com/jp/
http://store.tavix.jp/Special/Compare/Computer/Relmo/index.html

また「クレジットカード」で検索して1ページ目に出てくるサイトには
綺麗なサイトが多いので、こちらも参考にして頂きたいです。

【サイズの横幅について】

現在の横幅はぴったり950pxですが、
980px前後までであれば、横幅が大きくなっても構いません。
横幅が現在よりも小さくなるのは不可です。

ただし、ヘッダー部分とフッター部分は下記サイトのように横全体に広がっているデザインが希望です。
http://www.qrt.co.jp/ordercard/index.html

■ 納品ファイルの希望

第一希望 フォトショップ形式 + BMP形式
第二希望 イラストレーター形式 + BMP形式

■ 進め方

弊社の希望するイメージに近い提案を1つ(場合によって複数)選択させて頂きます。希望に近づけるために、修正要望を個別にさせて頂くこともあります。コンペ方式のため、修正後に当選されない場合も、どうかご了承ください。

■ その他/注意点

選択させて頂いたウェブデザインの著作権(財産権)等の扱いはTezukuri利用規約に従い、弊社に譲渡をお願いします。フォントや画像素材などを利用する場合は上記利用用途に使用できることを確認し、第三者の知的財産権等に注意して下さい。
■リニューアルによる変更点
今回のリニューアルではデザイン面だけでなくシステム面も強化するため
トップページのデザインが一部変更になります。
変更点は添付ファイルにまとめました。
なので現在のトップページのデザイン( http://www.hoshizora-cardnavi.com/
ではなく添付ファイル内のデザインを元にデザインをしてください。

```html
<!DOCTYPE html>
<html lang="ja">
<head>
<meta charset="utf-8">
<title>カード選びナビ広場</title>
<link href="https://fonts.googleapis.com/css2?family=Noto+Sans+JP:wght@400;700&family=M+PLUS+Rounded+1c:wght@700;800&display=swap" rel="stylesheet">
<style>
:root{
  --blue:#1b6fc6;
  --blue-dark:#0f4f99;
  --blue-light:#e8f2fc;
  --orange:#f08a12;
  --orange-dark:#d9650a;
  --yellow:#ffe27a;
  --text:#333;
  --muted:#777;
  --line:#cfdde9;
  --bg:#ffffff;
  --foot:#eef1f4;
  --gold:#c8a24a;
}
*{box-sizing:border-box;margin:0;padding:0}
html,body{width:1200px;height:2980px;overflow:hidden;background:var(--bg)}
body{font-family:"Noto Sans JP",sans-serif;color:var(--text);font-size:12px;position:relative}
.abs{position:absolute}
ul{list-style:none}

/* header */
.site-header{left:0;top:0;width:1200px;height:168px;background:linear-gradient(#fff,#eef5fc);border-bottom:1px solid var(--line)}
.logo{left:48px;top:52px;font-family:"M PLUS Rounded 1c",sans-serif;font-weight:800;font-size:30px;color:var(--orange);display:flex;align-items:center;gap:10px}
.logo i{display:block;width:18px;height:18px;border-radius:50%;background:var(--blue)}
.tagline{left:360px;top:46px;font-family:"M PLUS Rounded 1c",sans-serif;font-weight:700;color:var(--blue);font-size:20px;line-height:28px}
.tagline em{color:var(--orange);font-style:normal}
.global-nav{left:48px;top:176px;width:1112px;height:36px;display:flex;background:linear-gradient(#3e8ad8,var(--blue-dark));border-radius:3px}
.global-nav a{flex:1;color:#fff;font-weight:700;font-size:12px;text-align:center;line-height:36px;border-right:1px solid rgba(255,255,255,.35)}
.global-nav a:last-child{border-right:0}

/* main column */
.main{left:48px;top:0;width:840px;height:2680px}
.intro{left:0;top:228px;width:840px;height:40px;border:1px solid var(--line);background:var(--blue-light);padding:0 12px;font-size:12px;line-height:38px;color:var(--blue-dark)}
.news{left:0;top:278px;width:840px}
.news h3{font-size:13px;color:var(--blue-dark);border-bottom:1px dotted var(--line);padding-bottom:3px;margin-bottom:3px}
.news li{font-size:12px;line-height:22px;display:flex;gap:16px;border-bottom:1px dotted #e3e9ef}
.news time{color:var(--muted);width:120px}
.news a{color:var(--blue);text-decoration:underline}
.sec-head{position:absolute;left:0;width:840px;height:32px;background:linear-gradient(90deg,var(--blue),#5aa3e6 60%,#dceefc);border-radius:3px;color:#fff;font-weight:700;font-size:14px;line-height:32px;padding-left:14px}
.sec-head span{position:absolute;right:12px;color:var(--blue);font-style:italic;font-size:13px}
.fee-cols{left:0;top:424px;width:840px;display:grid;grid-template-columns:repeat(4,1fr);gap:14px}
.fee-col{border:1px solid var(--line);border-radius:4px;height:190px;text-align:center;padding-top:12px;background:#fff}
.fee-col b{display:block;color:var(--orange-dark);font-size:14px;line-height:20px}
.fee-col small{display:block;color:var(--muted);font-size:11px;line-height:16px}
.fee-col .card{margin:8px auto 12px;width:130px;height:82px}
.card{border-radius:5px;background:linear-gradient(135deg,#9dc0e6,#4b7fb8)}
.card.gold{background:linear-gradient(135deg,#f1dd9b,var(--gold))}
.card.silver{background:linear-gradient(135deg,#eef0f3,#9aa3ad)}
.card.black{background:linear-gradient(135deg,#555,#111)}
.card.green{background:linear-gradient(135deg,#bfe3b4,#4d9a53)}
.btn{display:inline-block;background:linear-gradient(var(--orange),var(--orange-dark));color:#fff;font-weight:700;font-size:12px;border-radius:3px;padding:4px 16px}
.btn.blue{background:linear-gradient(#4a98e2,var(--blue-dark))}
.pr-box{left:0;top:630px;width:840px;height:110px;border:1px dashed var(--line);display:grid;grid-template-columns:1fr 1fr;gap:20px;padding:14px 16px}
.pr-item{display:flex;gap:14px;font-size:12px;line-height:19px;color:var(--muted)}
.pr-item b{color:var(--blue-dark)}
.pr-item .card{width:124px;height:78px;flex:none}
.pickup-title{left:0;top:806px;width:840px;border-bottom:2px solid var(--orange);font-weight:700;color:var(--orange-dark);font-size:14px;padding-bottom:4px}
.tiles{left:0;width:840px;display:grid;grid-template-columns:repeat(5,1fr);gap:14px}
.tile{height:170px;font-size:12px;line-height:17px;color:var(--blue)}
.tile .ph{height:126px;border:1px solid var(--line);background:linear-gradient(#dbeaf7,#b9d3ea);margin-bottom:6px}

/* search */
.search{left:0;top:1262px;width:840px;height:604px;border:1px solid var(--line);padding:14px 18px;background:#fbfdff}
.search h4{font-size:13px;color:var(--blue-dark);margin:12px 0 6px;border-bottom:1px dotted var(--line);padding-bottom:3px}
.search h4:first-child{margin-top:0}
.checks{display:grid;grid-template-columns:repeat(4,1fr);row-gap:8px;font-size:12px;line-height:16px}
.checks label{display:flex;align-items:center;gap:6px}
.checks label::before{content:"";width:11px;height:11px;border:1px solid #888;background:#fff;flex:none}
.select{display:inline-block;width:180px;height:24px;border:1px solid #999;font-size:12px;padding-left:6px;line-height:22px;background:#fff}
.keyword{display:inline-block;width:420px;height:24px;border:1px solid #999;background:#fff;font-size:12px;color:#aaa;padding-left:6px;line-height:22px}
.arrows{left:330px;top:1884px}
.result{left:520px;top:1930px;font-size:13px;color:var(--muted)}
.result b{color:var(--orange-dark);font-size:24px}
.search-btn{left:270px;top:1978px;width:300px;height:42px;border-radius:4px;background:linear-gradient(var(--orange),var(--orange-dark));color:#fff;font-weight:700;font-size:15px;text-align:center;line-height:42px}
.small-link{font-size:12px;color:var(--blue);text-decoration:underline;left:0;width:840px;text-align:center}

/* compare */
.compare{left:0;top:2126px;width:840px;display:grid;grid-template-columns:1fr 1fr;gap:18px}
.cmp{height:240px;border:1px solid var(--line);border-radius:4px;padding:16px;text-align:center;background:#fff}
.cmp-title{font-size:13px;font-weight:700;color:var(--blue-dark);margin-bottom:18px}
.cmp-body{display:flex;align-items:center;justify-content:center;gap:24px}
.cmp-body .card{width:140px;height:88px}
.vs{font-weight:800;font-size:26px;color:var(--orange)}
.cmp-note{font-size:11px;color:var(--muted);margin:14px 0 10px}

/* sidebar */
.sidebar{left:904px;top:0;width:256px;height:2680px}
.side-ad{position:absolute;left:0;width:256px;border-radius:4px;overflow:hidden}
.side-ad.dark{background:linear-gradient(#2a2a30,#0d0d10);color:#fff;padding:18px}
.rank{top:500px;height:624px;border:1px solid var(--line);background:#fff}
.rank h3{background:linear-gradient(var(--yellow),#f7c440);color:#6b4500;font-size:13px;padding:9px 12px}
.rank li{display:flex;gap:10px;align-items:center;font-size:12px;height:46px;padding:0 12px;border-bottom:1px dotted var(--line)}
.rank li i{font-style:normal;display:inline-block;width:20px;height:20px;border-radius:50%;background:var(--orange);color:#fff;text-align:center;line-height:20px;font-size:11px;flex:none}
.rank li small{margin-left:auto;color:var(--muted);font-size:10px}
.brand-row{display:flex;gap:8px;padding:12px}
.brand-row span{border:1px solid var(--line);padding:4px 8px;font-weight:700;font-size:11px;color:var(--blue-dark)}
.ad-text{font-weight:700;text-align:center}
.mini-list li{font-size:11px;line-height:22px;border-bottom:1px dotted var(--line);color:var(--blue)}

/* footer */
.site-footer{left:0;top:2700px;width:1200px;height:244px;background:var(--foot);border-top:3px solid var(--blue)}
.foot-about{left:48px;top:22px;width:420px;font-size:11px;line-height:19px;color:var(--muted)}
.foot-about b{display:block;color:var(--text);font-size:13px;margin-bottom:6px}
.foot-col{top:22px;width:190px;font-size:11px;line-height:22px;color:var(--blue)}
.foot-col b{display:block;color:var(--text);font-size:12px;margin-bottom:4px}
.copyright{left:0;top:2944px;width:1200px;height:36px;background:var(--blue-dark);color:#fff;font-size:11px;text-align:center;line-height:36px}
</style>
</head>
<body>
<header class="site-header abs">
  <div class="logo abs"><i></i>カード選びナビ広場</div>
  <p class="tagline abs"><em>ライフスタイル</em>にあった<br>最適な<em>クレジットカード</em>を探そう！</p>
</header>
<nav class="global-nav abs">
  <a>カテゴリーから探す</a><a>一覧から比較検討</a><a>一覧表で比較</a><a>ブログ</a><a>クレジットカードを知る</a>
</nav>

<main class="main abs">
  <p class="intro abs">クレジットカードの比較サイトへようこそ。年会費・ポイント・特典などの条件からあなたにぴったりの一枚を楽しく探せます。</p>
  <section class="news abs">
    <h3>新着情報</h3>
    <ul>
      <li><time>2013年04月01日</time><a>人気カードの特典情報を更新しました</a></li>
      <li><time>2013年03月25日</time><a>年会費無料カードの比較ページを追加しました</a></li>
      <li><time>2013年03月18日</time><a>ゴールドカード特集を公開しました</a></li>
    </ul>
  </section>

  <h2 class="sec-head" style="top:384px">年会費別 当サイト人気クレジットカード<span>Popular</span></h2>
  <div class="fee-cols abs">
    <div class="fee-col"><b>年会費無料</b><small>スタンダードカード</small><div class="card" role="img" aria-label="年会費無料カードの券面"></div><span class="btn">詳しく見る</span></div>
    <div class="fee-col"><b>1円〜1,000円</b><small>みなと信販カード</small><div class="card silver" role="img" aria-label="年会費1,000円以下カードの券面"></div><span class="btn">詳しく見る</span></div>
    <div class="fee-col"><b>2,000円〜5,000円</b><small>ゴールドカード</small><div class="card gold" role="img" aria-label="年会費5,000円以下カードの券面"></div><span class="btn">詳しく見る</span></div>
    <div class="fee-col"><b>1万円以上</b><small>プラチナカード</small><div class="card black" role="img" aria-label="年会費1万円以上カードの券面"></div><span class="btn">詳しく見る</span></div>
  </div>
  <div class="pr-box abs">
    <div class="pr-item"><div class="card" role="img" aria-label="おすすめカードの券面"></div><p><b>入会特典でポイントが貯まる</b><br>人気のスタンダードカード。<br>普段の買い物でポイント2倍。</p></div>
    <div class="pr-item"><div class="card green" role="img" aria-label="おすすめカードの券面"></div><p><b>ネット通販でお得に使える</b><br>年会費無料のカード。<br>電子マネーへのチャージも対応。</p></div>
  </div>

  <h2 class="sec-head" style="top:762px">クレジットカードを知る<span>Knowledge</span></h2>
  <p class="pickup-title abs">おすすめ記事をピックアップ</p>
  <div class="tiles abs" style="top:840px">
    <div class="tile"><div class="ph" role="img" aria-label="記事のイメージ"></div>カードの選び方の基本</div>
    <div class="tile"><div class="ph" role="img" aria-label="記事のイメージ"></div>ポイントを貯めるコツ</div>
    <div class="tile"><div class="ph" role="img" aria-label="記事のイメージ"></div>審査の流れを解説</div>
    <div class="tile"><div class="ph" role="img" aria-label="記事のイメージ"></div>安全に使うための注意点</div>
    <div class="tile"><div class="ph" role="img" aria-label="記事のイメージ"></div>紛失時の対処法</div>
  </div>
  <div class="tiles abs" style="top:1024px">
    <div class="tile"><div class="ph" role="img" aria-label="記事のイメージ"></div>海外旅行保険とは</div>
    <div class="tile"><div class="ph" role="img" aria-label="記事のイメージ"></div>電子マネーの活用法</div>
    <div class="tile"><div class="ph" role="img" aria-label="記事のイメージ"></div>リボ払いの仕組み</div>
    <div class="tile"><div class="ph" role="img" aria-label="記事のイメージ"></div>キャッシングの注意</div>
    <div class="tile"><div class="ph" role="img" aria-label="記事のイメージ"></div>ゴールドカードの魅力</div>
  </div>

  <h2 class="sec-head" style="top:1220px">クレジットカードを条件から絞り込んで探す<span>Search</span></h2>
  <form class="search abs">
    <h4>サービス・特典</h4>
    <div class="checks">
      <label>ポイント高還元</label><label>マイルが貯まる</label><label>ETCカード</label><label>家族カード</label>
      <label>海外旅行保険</label><label>国内旅行保険</label><label>ショッピング保険</label><label>空港ラウンジ</label>
      <label>ガソリン割引</label><label>ネット通販優待</label><label>即日発行</label><label>学生向け</label>
    </div>
    <h4>年会費</h4>
    <div class="checks">
      <label>永年無料</label><label>初年度無料</label><label>条件付き無料</label><label>1,000円以下</label>
      <label>5,000円以下</label><label>10,000円以下</label><label>10,000円以上</label><label>こだわらない</label>
    </div>
    <h4>発行スピード</h4>
    <div class="checks"><label>即日</label><label>1週間以内</label><label>2週間以内</label><label>こだわらない</label></div>
    <h4>電子マネー</h4>
    <div class="checks">
      <label>電子マネーA</label><label>電子マネーB</label><label>電子マネーC</label><label>電子マネーD</label>
      <label>電子マネーE</label><label>こだわらない</label>
    </div>
    <h4>支払い方法</h4>
    <div class="checks"><label>一括払い</label><label>分割払い</label><label>リボ払い</label><label>ボーナス払い</label></div>
    <h4>年齢</h4>
    <span class="select">年齢を選択 ▼</span>
    <h4>国際ブランド</h4>
    <div class="checks">
      <label>VELA</label><label>Mercury</label><label>KRB</label><label>Aurelia</label>
      <label>Dinara</label><label>こだわらない</label>
    </div>
    <h4>キーワード</h4>
    <span class="keyword">カード名やキーワードを入力</span>
  </form>
  <svg class="arrows abs" width="180" height="70" viewBox="0 0 180 70" aria-hidden="true">
    <path d="M30 8 L90 36 L150 8" fill="none" stroke="#f6b25a" stroke-width="10" stroke-linecap="round" stroke-linejoin="round"/>
    <path d="M30 32 L90 60 L150 32" fill="none" stroke="#f08a12" stroke-width="10" stroke-linecap="round" stroke-linejoin="round"/>
  </svg>
  <p class="result abs">該当カード <b>67</b> 件</p>
  <div class="search-btn abs">この条件で検索する</div>
  <p class="abs small-link" style="top:2036px">クレジットカードを一覧から比較検討する場合はこちら</p>

  <h2 class="sec-head" style="top:2082px">クレジットカード比較<span>Compare</span></h2>
  <div class="compare abs">
    <div class="cmp"><p class="cmp-title">スタンダードカード比較</p><div class="cmp-body"><div class="card" role="img" aria-label="比較カードの券面"></div><span class="vs">VS</span><div class="card green" role="img" aria-label="比較カードの券面"></div></div><p class="cmp-note">年会費無料の定番カード同士を比較</p><span class="btn">比較する</span></div>
    <div class="cmp"><p class="cmp-title">コンビニでお得なクレジットカード比較</p><div class="cmp-body"><div class="card silver" role="img" aria-label="比較カードの券面"></div><span class="vs">VS</span><div class="card" role="img" aria-label="比較カードの券面"></div></div><p class="cmp-note">毎日の買い物で還元率が高いのは？</p><span class="btn">比較する</span></div>
    <div class="cmp"><p class="cmp-title">ゴールドカード比較</p><div class="cmp-body"><div class="card gold" role="img" aria-label="比較カードの券面"></div><span class="vs">VS</span><div class="card gold" role="img" aria-label="比較カードの券面"></div></div><p class="cmp-note">特典と年会費のバランスを比較</p><span class="btn">比較する</span></div>
    <div class="cmp"><p class="cmp-title">ポイントが貯まるクレジットカード比較</p><div class="cmp-body"><div class="card green" role="img" aria-label="比較カードの券面"></div><span class="vs">VS</span><div class="card silver" role="img" aria-label="比較カードの券面"></div></div><p class="cmp-note">ポイントの貯まりやすさを徹底比較</p><span class="btn">比較する</span></div>
  </div>
  <p class="abs small-link" style="top:2640px">クレジットカード比較の一覧はこちらからご覧いただけます</p>
</main>

<aside class="sidebar abs">
  <div class="side-ad dark" style="top:228px;height:256px">
    <p style="font-size:11px;color:#ccc">プレミアムな一枚</p>
    <p style="font-weight:700;font-size:15px;color:var(--gold);margin:6px 0 16px">VELA プラチナカード</p>
    <div class="card black" style="width:180px;height:112px;margin:0 auto;border:1px solid #666" role="img" aria-label="プラチナカードの券面"></div>
    <p style="margin-top:18px;font-size:11px;color:#bbb">上質なサービスと特典をあなたに</p>
  </div>
  <div class="side-ad rank">
    <h3>クレジットカード人気ランキング</h3>
    <ul>
      <li><i>1</i>年会費無料のカード<small>詳細</small></li><li><i>2</i>ポイント高還元カード<small>詳細</small></li><li><i>3</i>マイルが貯まるカード<small>詳細</small></li>
      <li><i>4</i>ゴールドカード<small>詳細</small></li><li><i>5</i>学生向けカード<small>詳細</small></li><li><i>6</i>即日発行カード<small>詳細</small></li>
      <li><i>7</i>ETC専用カード<small>詳細</small></li><li><i>8</i>海外旅行向けカード<small>詳細</small></li><li><i>9</i>電子マネー対応<small>詳細</small></li><li><i>10</i>女性向けカード<small>詳細</small></li>
    </ul>
    <div class="brand-row"><span>VELA</span><span>Mercury</span><span>KRB</span></div>
    <div style="text-align:center;margin-top:4px"><span class="btn blue">ランキングをもっと見る</span></div>
  </div>
  <div class="side-ad" style="top:1140px;height:170px;background:linear-gradient(#dff0ff,#a9d2f5)" role="img" aria-label="入会キャンペーン告知の画像">
    <p class="ad-text" style="padding-top:52px;color:var(--orange-dark);font-size:30px">16,000円</p>
    <p class="ad-text" style="color:var(--blue-dark);font-size:14px">相当プレゼント</p>
  </div>
  <div class="side-ad" style="top:1326px;height:96px;background:linear-gradient(#fff7e0,#ffd77a)" role="img" aria-label="ポイント還元キャンペーンの画像">
    <p class="ad-text" style="padding-top:36px;color:#b35b00;font-size:16px">ポイント3倍キャンペーン</p>
  </div>
  <div class="side-ad" style="top:1438px;height:120px;border:1px solid var(--line);padding:14px 16px;background:#fff">
    <p style="font-size:11px;color:var(--blue-dark)">みなと信販カード</p>
    <p style="font-weight:700;font-size:20px;color:var(--blue-dark);margin:4px 0 10px">エブリワン</p>
    <span class="btn blue">詳細はこちら</span>
  </div>
  <div class="side-ad" style="top:1574px;height:130px;background:linear-gradient(#ffe9e9,#f4a5a5)" role="img" aria-label="ヨロズカード入会特典の画像">
    <p class="ad-text" style="padding-top:40px;color:#a71e1e;font-size:17px">ヨロズカード</p>
    <p class="ad-text" style="color:#a71e1e;font-size:12px;margin-top:6px">新規入会でポイント進呈</p>
  </div>
  <div class="side-ad" style="top:1720px;height:290px;background:#fff;border:1px solid var(--line);padding:16px">
    <div class="card gold" style="width:160px;height:100px;margin:0 auto" role="img" aria-label="ゴールドカードの券面"></div>
    <p style="text-align:center;margin:12px 0 8px;font-size:12px;color:var(--text);font-weight:700">ワンランク上のゴールドカード</p>
    <ul class="mini-list">
      <li>空港ラウンジが無料で使える</li><li>旅行保険が自動で付帯</li><li>利用枠が大きく安心</li><li>専用デスクでサポート</li>
    </ul>
  </div>
  <div class="side-ad dark" style="top:2026px;height:634px">
    <p style="font-weight:700;font-size:16px;color:var(--gold)">Aurelia Gold Card</p>
    <p style="font-size:11px;color:#bbb;margin-top:4px">ゴールドカードの新しいスタンダード</p>
    <div class="card gold" style="width:210px;height:132px;margin:36px auto 30px" role="img" aria-label="ゴールドカードの券面"></div>
    <p style="font-size:12px;color:#ddd;line-height:20px">充実の旅行保険と空港ラウンジ。<br>上質なサービスを日常に。</p>
    <ul style="margin-top:24px;font-size:12px;line-height:28px;color:#ccc">
      <li>✓ 国内外の空港ラウンジ無料</li>
      <li>✓ 最高1億円の旅行傷害保険</li>
      <li>✓ ポイントに有効期限なし</li>
      <li>✓ 24時間の専用サポート</li>
      <li>✓ 入会初年度の特典あり</li>
    </ul>
    <div style="text-align:center;margin-top:40px"><span class="btn">詳しくはこちら</span></div>
  </div>
</aside>

<footer class="site-footer abs">
  <div class="foot-about abs">
    <b>カード選びナビ広場について</b>
    <p>当サイトはクレジットカードの年会費・ポイント・特典などを分かりやすく比較し、あなたに合った一枚を探すお手伝いをする情報サイトです。掲載している情報は各カード会社の公式情報をもとにしていますが、内容は予告なく変更される場合があります。お申し込みの際は必ず各社の最新情報をご確認ください。</p>
  </div>
  <div class="foot-col abs" style="left:540px">
    <b>カテゴリー</b>
    <p>年会費無料カード</p><p>ゴールドカード</p><p>マイルが貯まるカード</p><p>学生向けカード</p><p>即日発行カード</p>
  </div>
  <div class="foot-col abs" style="left:740px">
    <b>コンテンツ</b>
    <p>一覧から比較検討</p><p>一覧表で比較</p><p>クレジットカードを知る</p><p>ブログ</p><p>人気ランキング</p>
  </div>
  <div class="foot-col abs" style="left:960px">
    <b>サイト情報</b>
    <p>運営者情報</p><p>プライバシーポリシー</p><p>お問い合わせ</p><p>サイトマップ</p>
  </div>
</footer>
<div class="copyright abs">Copyright © 2013 カード選びナビ広場 All Rights Reserved.</div>
</body>
</html>
```